Dornel Letterhead

Hi I really like the attached pictures for our business cards could you please look at designing something similar for our letterheads and stationary.

The details on our letterhead will be

Dornel Pty Ltd
ABN 847 216 350
PO Box 7184
Kellmont NSW 2190
0468 137 926
office"dornel.com.au

```html
<!DOCTYPE html>
<html lang="en">
<head>
<meta charset="utf-8">
<title>Dornel Letterhead</title>
<link rel="stylesheet" href="https://fonts.googleapis.com/css2?family=Open+Sans:wght@400;600;700;800&display=swap">
<style>
  :root {
    --ink: #0a0a0a;
    --paper: #ffffff;
    --paper-shade: #ececec;
    --brand-blue: #3a6db5;
    --brand-blue-deep: #1f4c8f;
    --muted: #8a8a8a;
    --footer-text: #e6e6e6;
  }
  * { margin: 0; padding: 0; box-sizing: border-box; }
  html, body { width: 1079px; height: 1200px; overflow: hidden; }
  body { font-family: "Open Sans", Arial, sans-serif; background: var(--paper); }
  .letterhead {
    position: relative;
    width: 1079px;
    height: 1200px;
    background: linear-gradient(180deg, var(--paper) 0%, var(--paper) 35%, var(--paper-shade) 100%);
    overflow: hidden;
  }
  .brand {
    position: absolute;
    left: 84px;
    top: 78px;
  }
  .brand-name {
    display: flex;
    align-items: center;
    gap: 10px;
    font-weight: 800;
    font-size: 50px;
    line-height: 1;
    letter-spacing: -1px;
    color: var(--ink);
  }
  .brand-mark {
    width: 14px;
    height: 14px;
    background: var(--brand-blue);
  }
  .brand-tagline {
    margin-top: 6px;
    font-size: 14px;
    font-weight: 600;
    letter-spacing: 1.5px;
    color: var(--muted);
    text-transform: uppercase;
  }
  .footer-art {
    position: absolute;
    left: 0;
    bottom: 0;
    width: 1079px;
    height: 250px;
  }
  .footer-details {
    position: absolute;
    left: 540px;
    top: 1060px;
    font-size: 14px;
    line-height: 21px;
    color: var(--footer-text);
  }
  .footer-company { color: var(--brand-blue); font-weight: 700; }
  .footer-contact { display: flex; align-items: center; gap: 6px; }
  .footer-contact svg { width: 14px; height: 14px; }
</style>
</head>
<body>
<main class="letterhead">
  <header class="brand">
    <div class="brand-name"><span>Dornel</span><span class="brand-mark"></span></div>
    <div class="brand-tagline">Civil Projects</div>
  </header>

  <svg class="footer-art" viewBox="0 0 1079 250" xmlns="http://www.w3.org/2000/svg">
    <polygon points="400,40 1079,40 1079,250 330,250 385,150 330,60" fill="var(--ink)"/>
    <g role="img" aria-label="Blue patterned corner decoration">
      <polygon points="0,110 300,110 250,200 300,250 0,250" fill="var(--brand-blue-deep)"/>
      <polygon points="300,110 370,110 320,200 360,250 300,250 250,200" fill="var(--brand-blue)"/>
    </g>
  </svg>

  <footer class="footer-details">
    <div class="footer-company">Dornel Pty Ltd</div>
    <div>PO Box 7184, Kellmont NSW 2190 &nbsp;|&nbsp; ABN 847 216 350</div>
    <div class="footer-contact">
      <svg viewBox="0 0 24 24" aria-hidden="true"><path fill="var(--brand-blue)" d="M6.6 10.8a15 15 0 0 0 6.6 6.6l2.2-2.2c.3-.3.7-.4 1-.2 1.1.4 2.3.6 3.6.6.6 0 1 .4 1 1V20c0 .6-.4 1-1 1A17 17 0 0 1 3 4c0-.6.4-1 1-1h3.5c.6 0 1 .4 1 1 0 1.3.2 2.5.6 3.6.1.3 0 .7-.2 1z"/></svg>
      <span>0468 137 926 &nbsp;|</span>
      <svg viewBox="0 0 24 24" aria-hidden="true"><circle cx="12" cy="12" r="9" fill="none" stroke="var(--brand-blue)" stroke-width="2"/><path d="M3 12h18M12 3c3 3 3 15 0 18M12 3c-3 3-3 15 0 18" fill="none" stroke="var(--brand-blue)" stroke-width="1.5"/></svg>
      <span>dornel.com.au</span>
    </div>
  </footer>
</main>
</body>
</html>
```